nestliva - Ballon Design

I need a Ballon designed. Please use the psb file ballon_template.psb as template.

I would like to have a ballon designed similar to the file "example.png".
instead of the pellu tot logo please use my attached logo "nestliva logo.ai"

The text should be the same " IT'S A MOM" but the logo should be different.

I should look like more elegant. should be also white background. But for the design feel free.

thanks.

Please also add the webpage "www.nestliva.eu" on the ballon design.

```html
<!DOCTYPE html>
<html lang="en">
<head>
<meta charset="utf-8">
<title>nestliva – It's a Mom balloon</title>
<link rel="stylesheet" href="https://fonts.googleapis.com/css2?family=Playfair+Display:wght@500;900&display=swap">
<style>
  :root {
    --page-bg: #ffffff;
    --balloon-face: #ffffff;
    --balloon-rim: #d9dadc;
    --blush-pink: #f6c3d8;
    --brand-blue: #1f86c8;
  }
  html, body {
    margin: 0;
    padding: 0;
    overflow: hidden;
    background: var(--page-bg);
  }
  .canvas {
    position: relative;
    width: 1200px;
    height: 1200px;
    background: var(--page-bg);
    overflow: hidden;
  }
  .balloon-face {
    position: absolute;
    left: 0;
    top: 0;
  }
  .headline {
    position: absolute;
    left: 0;
    width: 1200px;
    top: 319px;
    margin: 0;
    text-align: center;
    font-family: "Playfair Display", Georgia, serif;
    font-weight: 900;
    font-size: 140px;
    line-height: 110px;
    color: var(--blush-pink);
  }
  .headline span { display: block; }
  .brand-name {
    position: absolute;
    left: 0;
    width: 1200px;
    top: 681px;
    margin: 0;
    text-align: center;
    font-family: "Playfair Display", Georgia, serif;
    font-weight: 900;
    font-size: 80px;
    line-height: 90px;
    color: var(--brand-blue);
  }
  .web-address {
    position: absolute;
    left: 0;
    width: 1200px;
    top: 788px;
    margin: 0;
    text-align: center;
    font-family: "Playfair Display", Georgia, serif;
    font-weight: 500;
    font-size: 28px;
    line-height: 36px;
    letter-spacing: 2px;
    color: var(--brand-blue);
  }
</style>
</head>
<body>
  <main class="canvas">
    <svg class="balloon-face" width="1200" height="1200" viewBox="0 0 1200 1200" aria-hidden="true">
      <circle cx="600" cy="545" r="360" fill="var(--balloon-face)" stroke="var(--balloon-rim)" stroke-width="6"/>
    </svg>
    <h1 class="headline">
      <span>It's</span>
      <span>a</span>
      <span>Mom</span>
    </h1>
    <p class="brand-name">nestliva</p>
    <p class="web-address">www.nestliva.eu</p>
  </main>
</body>
</html>
```